Soap Company Looking To Design New Soap Scent Boxes

we are looking to create a soap box similar to mr brindle. we would like the circle cut out on the top right corner of the box. we are looking for a design that will allow us to use different color base banners for different soap scents (like mr. brindle). we want the soap name scents to be large and readable on the bottom banner (like mr.brindle). we have included our brand figure (logo) and some previous older soap box designs that we were making before the brand figure. the box dims are attached.

```html
<!DOCTYPE html>
<html lang="en">
<head>
<meta charset="utf-8">
<title>Bramblewick – Soap Box Dieline, Plumeria</title>
<link rel="stylesheet" href="https://fonts.googleapis.com/css2?family=Alegreya:wght@400;500;800&family=Marcellus&family=Archivo+Black&family=Archivo:wght@800&display=swap">
<style>
  :root{
    --kraft:#e2c8a6;
    --band-red:#b00818;
    --ink:#1b110c;
    --cut:#2fe3ef;
    --bleed:#e3131b;
    --safe:#3ed40c;
    --dim-red:#f10d0d;
    --white:#ffffff;
    --cyan:#00f0ff;
    --magenta:#ff00f5;
    --yellow:#fff500;
    --black:#000000;
    --pantone:#a80a19;
  }
  html,body{margin:0;padding:0;width:1200px;height:1000px;overflow:hidden;background:var(--white);}
  .dieline{display:block;width:1200px;height:1000px;}
  .dim-label{font-family:"Archivo Black",sans-serif;font-size:68px;fill:var(--dim-red);text-anchor:middle;}
  .dim-arrow{stroke:var(--black);stroke-width:4;fill:none;}
  .legend-text{font-family:"Archivo",sans-serif;font-weight:800;font-size:29px;fill:var(--black);}
  .cut-line{stroke:var(--cut);stroke-width:2;fill:none;}
  .bleed-line{stroke:var(--bleed);stroke-width:1.6;fill:none;}
  .safe-line{stroke:var(--safe);stroke-width:1.6;fill:none;}
  .brand-name{font-family:"Alegreya",serif;font-weight:800;fill:var(--ink);text-anchor:middle;}
  .body-copy{font-family:"Alegreya",serif;font-weight:500;font-size:23px;fill:var(--ink);text-anchor:middle;}
  .tagline{font-family:"Alegreya",serif;font-weight:400;fill:var(--white);text-anchor:middle;}
  .scent-list{font-family:"Alegreya",serif;font-weight:500;font-size:16.5px;fill:var(--ink);text-anchor:middle;}
  .benefit-label{font-family:"Alegreya",serif;font-weight:400;font-size:19px;fill:var(--white);text-anchor:middle;}
  .scent-name{font-family:"Marcellus",serif;font-size:84px;fill:var(--white);text-anchor:middle;letter-spacing:2px;}
  .net-weight{font-family:"Alegreya",serif;font-size:16px;fill:var(--white);text-anchor:middle;}
  .side-motto{font-family:"Alegreya",serif;font-weight:500;font-size:22px;fill:var(--ink);text-anchor:middle;}
  .icon-line{stroke:var(--white);stroke-width:3;fill:none;stroke-linejoin:round;stroke-linecap:round;}
  .lotus-line{stroke:var(--ink);stroke-width:3;fill:none;stroke-linejoin:round;}
</style>
</head>
<body>
<svg class="dieline" viewBox="0 0 2100 1750" xmlns="http://www.w3.org/2000/svg">
  <defs>
    <marker id="arrow-head" viewBox="0 0 12 12" refX="11" refY="6" markerWidth="6" markerHeight="6" orient="auto-start-reverse">
      <path d="M0,0 L12,6 L0,12" fill="none" stroke="#000" stroke-width="2"/>
    </marker>
    <clipPath id="box-shape">
      <path d="M120,612 L120,385 Q120,290 215,290 L683,290 Q778,290 778,385 L778,460 L945,460 L972,572 L1000,607 L1560,607 L1588,572 L1615,460 L1830,460 L1830,1275 L1805,1305 L1778,1415 L1610,1415 L1610,1490 Q1610,1585 1515,1585 L1045,1585 Q950,1585 950,1490 L950,1415 L785,1415 L755,1305 L730,1275 L730,1268 L145,1268 L22,1240 L22,632 Z"/>
    </clipPath>
  </defs>

  <!-- Panel widths -->
  <g class="dimensions">
    <text class="dim-label" x="449" y="212">3.125"</text>
    <text class="dim-label" x="864" y="212">1.125"</text>
    <text class="dim-label" x="1280" y="212">3.125"</text>
    <text class="dim-label" x="1695" y="212">1.125"</text>
    <line class="dim-arrow" x1="170" y1="265" x2="728" y2="265" marker-start="url(#arrow-head)" marker-end="url(#arrow-head)"/>
    <line class="dim-arrow" x1="780" y1="265" x2="948" y2="265" marker-start="url(#arrow-head)" marker-end="url(#arrow-head)"/>
    <line class="dim-arrow" x1="1001" y1="265" x2="1560" y2="265" marker-start="url(#arrow-head)" marker-end="url(#arrow-head)"/>
    <line class="dim-arrow" x1="1612" y1="265" x2="1780" y2="265" marker-start="url(#arrow-head)" marker-end="url(#arrow-head)"/>
    <line class="dim-arrow" x1="1857" y1="660" x2="1857" y2="1216" marker-start="url(#arrow-head)" marker-end="url(#arrow-head)"/>
    <text class="dim-label" transform="translate(1910 938) rotate(90)">3.125"</text>
  </g>

  <!-- Colour legend -->
  <g class="colour-legend">
    <rect x="1884" y="272" width="44" height="44" rx="12" fill="var(--white)" stroke="#333" stroke-width="1.5"/>
    <text class="legend-text" x="1944" y="304">WHITE</text>
    <rect x="1884" y="344" width="44" height="44" rx="12" fill="var(--cyan)"/>
    <text class="legend-text" x="1944" y="377">CYAN</text>
    <rect x="1884" y="418" width="44" height="44" rx="12" fill="var(--magenta)"/>
    <text class="legend-text" x="1944" y="451">MAGENTA</text>
    <rect x="1884" y="490" width="44" height="44" rx="12" fill="var(--yellow)"/>
    <text class="legend-text" x="1944" y="523">YELLOW</text>
    <rect x="1884" y="560" width="44" height="44" rx="12" fill="var(--black)"/>
    <text class="legend-text" x="1944" y="593">BLACK</text>
    <rect x="1884" y="633" width="44" height="44" rx="12" fill="var(--pantone)"/>
    <text class="legend-text" x="1944" y="655">PANTONE</text>
    <text class="legend-text" x="1944" y="683">1805 C</text>
  </g>

  <!-- Box artwork -->
  <g class="box-artwork" clip-path="url(#box-shape)">
    <rect x="0" y="280" width="1840" height="1320" fill="var(--kraft)" role="img" aria-label="Kraft background with a faint hand-drawn leaf and herb pattern"/>
    <rect x="0" y="1050" width="1840" height="10" fill="var(--ink)"/>
    <rect x="0" y="1060" width="1840" height="166" fill="var(--band-red)"/>
  </g>
  <path class="cut-line" d="M120,612 L120,385 Q120,290 215,290 L683,290 Q778,290 778,385 L778,460 L945,460 L972,572 L1000,607 L1560,607 L1588,572 L1615,460 L1830,460 L1830,1275 L1805,1305 L1778,1415 L1610,1415 L1610,1490 Q1610,1585 1515,1585 L1045,1585 Q950,1585 950,1490 L950,1415 L785,1415 L755,1305 L730,1275 L730,1268 L145,1268 L22,1240 L22,632 Z"/>

  <!-- Fold and bleed lines -->
  <g class="bleed-lines">
    <path class="bleed-line" d="M145,632 L145,400 Q145,315 230,315 L670,315 Q755,315 755,400 L755,632"/>
    <line class="bleed-line" x1="145" y1="411" x2="755" y2="411"/>
    <line class="bleed-line" x1="45" y1="632" x2="1805" y2="632"/>
    <line class="bleed-line" x1="45" y1="1243" x2="1805" y2="1243"/>
    <line class="bleed-line" x1="145" y1="632" x2="145" y2="1243"/>
    <line class="bleed-line" x1="755" y1="632" x2="755" y2="1243"/>
    <line class="bleed-line" x1="975" y1="607" x2="975" y2="1463"/>
    <line class="bleed-line" x1="1585" y1="607" x2="1585" y2="1463"/>
    <path class="bleed-line" d="M45,655 L145,632 M45,655 L45,1222 L145,1243"/>
    <path class="bleed-line" d="M755,632 L755,485 L928,485 L952,585 L975,607"/>
    <path class="bleed-line" d="M1585,607 L1610,585 L1635,485 L1805,485 L1805,1243"/>
    <path class="bleed-line" d="M755,1243 L755,1268 L780,1290 L808,1392 L950,1392"/>
    <path class="bleed-line" d="M1585,1392 L1755,1392 L1780,1290 L1805,1268 L1805,1243"/>
    <path class="bleed-line" d="M975,1463 L975,1475 Q975,1560 1060,1560 L1500,1560 Q1585,1560 1585,1475 L1585,1463 Z"/>
  </g>

  <!-- Safe zones -->
  <g class="safe-lines">
    <rect class="safe-line" x="168" y="338" width="562" height="49" rx="20"/>
    <rect class="safe-line" x="168" y="436" width="562" height="171"/>
    <rect class="safe-line" x="168" y="657" width="562" height="561"/>
    <rect class="safe-line" x="779" y="657" width="171" height="561"/>
    <rect class="safe-line" x="999" y="657" width="562" height="561"/>
    <rect class="safe-line" x="1610" y="657" width="171" height="561"/>
    <path class="safe-line" d="M70,675 L120,663 L120,1210 L70,1198 Z"/>
    <path class="safe-line" d="M779,510 L905,510 L940,607 L779,607 Z"/>
    <path class="safe-line" d="M1655,510 L1781,510 L1781,607 L1620,607 Z"/>
    <path class="safe-line" d="M795,1268 L950,1268 L950,1365 L822,1365 Z"/>
    <path class="safe-line" d="M1610,1268 L1770,1268 L1740,1365 L1610,1365 Z"/>
    <rect class="safe-line" x="999" y="1268" width="562" height="170"/>
    <rect class="safe-line" x="999" y="1488" width="562" height="48" rx="20"/>
  </g>

  <!-- Top tuck flap: brand name, upside down -->
  <g class="top-flap-brand" transform="rotate(180 449 522)">
    <text class="brand-name" x="449" y="540" font-size="56">Bramblewick</text>
  </g>

  <!-- Back panel -->
  <g class="back-panel">
    <text class="brand-name" x="449" y="725" font-size="76">Bramblewick</text>
    <path d="M215,771 Q449,748 682,771 Q449,794 215,771 Z" fill="var(--ink)"/>
    <text class="tagline" x="449" y="778" font-size="21">Cold Pressed Artisan Soap</text>
    <text class="body-copy" x="449" y="830">Our Bath Soaps collection are infused with</text>
    <text class="body-copy" x="449" y="856">All-Organic ingredients. Including Coconut Oil,</text>
    <text class="body-copy" x="449" y="882">Canola Oil, Soybean Oil, Shea Butter, Water,</text>
    <text class="body-copy" x="449" y="908">Sodium Hydroxide (Lye) Olive Pomace Oil,</text>
    <text class="body-copy" x="449" y="934">Sunflower Oil, Fragrance.</text>
    <text class="body-copy" x="449" y="993" font-size="27">This is Nature in a Bar!</text>

    <g class="benefit-icon" role="img" aria-label="Raised hand icon">
      <path class="icon-line" d="M232,1140 L232,1098 Q232,1090 239,1090 Q245,1090 245,1098 L245,1088 Q245,1080 251,1080 Q257,1080 257,1088 L257,1096 Q257,1088 263,1088 Q269,1088 269,1096 L269,1140 Q269,1152 250,1152 Q232,1152 232,1140 Z"/>
      <path class="icon-line" d="M250,1136 Q240,1128 244,1122 Q248,1118 250,1124 Q252,1118 256,1122 Q260,1128 250,1136 Z"/>
    </g>
    <text class="benefit-label" x="249" y="1184">Handmade</text>
    <g class="benefit-icon" role="img" aria-label="Hand holding leaves icon">
      <path class="icon-line" d="M414,1128 L414,1146 L422,1146 Q440,1152 460,1146 L484,1132 Q486,1126 478,1127 L458,1136 L440,1136"/>
      <path class="icon-line" d="M449,1126 L449,1100 M449,1112 Q432,1112 428,1100 Q440,1096 449,1108 M449,1108 Q458,1096 470,1100 Q466,1112 449,1112"/>
      <path class="icon-line" d="M449,1094 Q443,1088 449,1080 Q455,1088 449,1094 Z"/>
    </g>
    <text class="benefit-label" x="449" y="1184">All-Natural</text>
    <text class="benefit-label" x="449" y="1203">Ingredients</text>
    <g class="benefit-icon" role="img" aria-label="Soap bar with bubbles icon">
      <rect class="icon-line" x="614" y="1098" width="50" height="40" rx="14" transform="rotate(-25 639 1118)"/>
      <circle class="icon-line" cx="660" cy="1145" r="6"/>
      <circle class="icon-line" cx="668" cy="1092" r="5"/>
    </g>
    <text class="benefit-label" x="641" y="1184">Variety of</text>
    <text class="benefit-label" x="641" y="1203">Soap Scents</text>
  </g>

  <!-- Left side panel: scent list -->
  <g class="scent-panel">
    <path d="M768,678 Q865,660 962,678 Q865,696 768,678 Z" fill="var(--ink)"/>
    <text class="tagline" x="865" y="683" font-size="13">AVAILABLE SCENTS</text>
    <text class="scent-list" x="865" y="714">Cedarwood Tea Tree</text>
    <text class="scent-list" x="865" y="736">Charcoal Aloe</text>
    <text class="scent-list" x="865" y="758">Cool Water</text>
    <text class="scent-list" x="865" y="779">Dead Sea Scrub</text>
    <text class="scent-list" x="865" y="801">Eucalyptus Aloe</text>
    <text class="scent-list" x="865" y="823">Hydrangea</text>
    <text class="scent-list" x="865" y="845">Jasmine Lime Scrub</text>
    <text class="scent-list" x="865" y="866">Mango Papaya</text>
    <text class="scent-list" x="865" y="888">Mountain Air</text>
    <text class="scent-list" x="865" y="910">Nag Champa</text>
    <text class="scent-list" x="865" y="932">Plumeria</text>
    <text class="scent-list" x="865" y="953">Raspberry Rush</text>
    <text class="scent-list" x="865" y="975">Raspberry Vanilla</text>
    <text class="scent-list" x="865" y="997">Sandalwood Rose</text>
    <text class="scent-list" x="865" y="1019">Tangerine Grapefruit</text>
    <text class="scent-list" x="865" y="1040">Wild Passion</text>
  </g>

  <!-- Front panel -->
  <g class="front-panel">
    <text class="brand-name" x="1280" y="965" font-size="88">Bramblewick</text>
    <circle cx="1483" cy="735" r="68" fill="none" stroke="var(--bleed)" stroke-width="1.6"/>
    <circle cx="1483" cy="735" r="44" fill="var(--white)" stroke="var(--cut)" stroke-width="2"/>
    <path d="M1015,1055 Q1280,1025 1545,1055 Q1280,1085 1015,1055 Z" fill="var(--ink)"/>
    <text class="tagline" x="1280" y="1063" font-size="23">Cold Pressed Artisan Soap</text>
    <text class="scent-name" x="1280" y="1162">PLUMERIA</text>
    <text class="net-weight" x="1280" y="1208">Net Wt. 5oz (140g)</text>
  </g>

  <!-- Right side panel -->
  <g class="motto-panel">
    <g role="img" aria-label="Lotus flower line icon">
      <path class="lotus-line" d="M1697,838 Q1676,810 1697,762 Q1718,810 1697,838 Z"/>
      <path class="lotus-line" d="M1697,838 Q1660,830 1656,784 Q1684,792 1690,812"/>
      <path class="lotus-line" d="M1697,838 Q1734,830 1738,784 Q1710,792 1704,812"/>
      <path class="lotus-line" d="M1648,828 Q1670,846 1697,840 Q1724,846 1746,828"/>
    </g>
    <text class="side-motto" x="1695" y="877">REJUVENATE</text>
    <text class="side-motto" x="1695" y="907">YOUR MIND,</text>
    <text class="side-motto" x="1695" y="937">BODY and</text>
    <text class="side-motto" x="1695" y="967">SOUL</text>
    <g role="img" aria-label="Recycling and disposal symbols">
      <path d="M1690,1210 L1700,1192 L1710,1210 Z" fill="none" stroke="var(--white)" stroke-width="3"/>
      <circle cx="1735" cy="1201" r="9" fill="none" stroke="var(--white)" stroke-width="3"/>
      <rect x="1762" y="1194" width="12" height="15" fill="none" stroke="var(--white)" stroke-width="3"/>
    </g>
  </g>

  <!-- Bottom flap brand name -->
  <g class="bottom-flap-brand">
    <text class="brand-name" x="1280" y="1372" font-size="60">Bramblewick</text>
  </g>
</svg>
</body>
</html>
```